Dixie Ore Website 3 Page Concept

We need a concept design for a company in Birmingham, AL called Dixie Ore Smeltery. We buy/sell precious metals, coins, fine watches, and jewelry. The current website can be found here: https://www.dixieoresmeltery.com. We're looking to modernize the website, drawing inspiration from the websites QUOLTA (https://www.quolta.com/) and RT Ingotry (https://www.rtingotry.com/).

QUOLTA has a lot of the design qualities we're looking to integrate into our website, with a similar header (from the changing metal prices to the categories).

+Pages to Be Designed for Concept
Home Page
Products Page
Main Store Page

+Colors
Black, White, Sleek Grey (from attached file), "Gold" (Citrus from attached file)

**Main goal is for the website to be easy to navigate and user friendly.

Target Market(s)

Retail customers

Industry/Entity Type

Coin

Number of Pages Required

3 page

Requirements
Must have
• +Colors
• Black, White, Sleek Grey (from attached file), "Gold" (Citrus from attached file)
• +The website would have 3 main sections (Coins, Fine Watches, and Jewelry). :
• -E-commerce (shopping cart link, etc.)
• -Account sign in option on front page
• -Variable payment pricing for gold/silver items (wire/cash, Remitly Pay/CC, Coinvee(Zentacoin)) (like so: https://www.quolta.com/product/71820/1-oz-silver-round-heron?48213=2)
• - Social media buttons (friendwall, snapreel)
• -Integrate same DOS logo from current website into new website design
• -Drop-down navigation menu towards the top for each 3 main sections (Hovering over them would list further categories), that lists further categories (can be taken from the left side of current site for example purposes: https://www.dixieoresmeltery.com)
• Additional: Mobile Friendly!
• **Main goal is for the website to be easy to navigate and user friendly.
Nice to have
• Videos and links (blog - like) on the home page

```html
<!DOCTYPE html>
<html lang="en">
<head>
<meta charset="utf-8">
<title>Dixie Ore Smeltery – 1.83ct K-Color I1 Brilliant Round</title>
<link href="https://fonts.googleapis.com/css2?family=Open+Sans:wght@400;600;700&family=Montserrat:wght@400;600;700&family=Josefin+Sans:wght@300;400&family=Cinzel:wght@700&display=swap" rel="stylesheet">
<style>
:root{
  --ink:#1c1f24;
  --topbar:#111316;
  --nav:#6c7a8e;
  --gold:#f6be2c;
  --gold-text:#e8a917;
  --paper:#ffffff;
  --mist:#f4f4f4;
  --line:#dedede;
  --muted:#6b6b6b;
  --pill:#55595f;
  --alert:#e0302a;
  --footer:#262a31;
  --footer-deep:#20242a;
  --footer-text:#c8cbd0;
}
*{box-sizing:border-box;margin:0;padding:0}
html,body{width:1200px;height:2941px;overflow:hidden}
body{position:relative;background:var(--paper);font-family:"Open Sans",Arial,sans-serif;color:var(--ink)}
.abs{position:absolute}

/* ticker */
.ticker{left:0;top:0;width:1200px;height:35px;background:var(--topbar);color:#fff;font:600 11px "Open Sans",sans-serif}
.ticker .rates{position:absolute;left:362px;top:0;height:35px;display:flex;align-items:center;gap:10px}
.ticker .up{color:var(--gold)}
.ticker .sep{width:1px;height:16px;background:#555}
.ticker .phone{position:absolute;right:56px;top:0;height:35px;display:flex;align-items:center;gap:8px}

/* promo bar */
.promo{left:0;top:35px;width:1200px;height:51px;background:var(--paper)}
.promo .note{position:absolute;left:80px;top:18px;font:700 10.5px "Open Sans",sans-serif;color:var(--gold-text);letter-spacing:.2px}
.search{position:absolute;left:613px;top:14px;width:328px;height:28px;display:flex}
.search input{flex:1;border:1px solid var(--line);font:12px "Open Sans",sans-serif;padding:0 10px;color:#999}
.search button{width:36px;border:0;background:var(--gold);display:flex;align-items:center;justify-content:center}
.login{position:absolute;left:1034px;top:14px;width:84px;height:28px;background:var(--gold);color:#333;font:700 12px "Montserrat",sans-serif;display:flex;align-items:center;justify-content:center}

/* main nav */
.mainnav{left:0;top:86px;width:1200px;height:90px;background:var(--nav)}
.brand{position:absolute;left:62px;top:12px;display:flex;align-items:center;gap:12px}
.brand .mark{width:66px;height:66px;border-radius:50%;background:#fff}
.brand .name{font:700 22px "Montserrat",sans-serif;color:#fff;letter-spacing:1px}
.menu{position:absolute;left:216px;top:0;height:90px;display:flex;align-items:center;gap:21px;list-style:none}
.menu li{font:700 11px "Montserrat",sans-serif;color:#fff;letter-spacing:.3px}
.menu li.on{color:var(--gold)}
.cart{position:absolute;left:1024px;top:30px}
.cart .count{position:absolute;left:22px;top:-6px;width:16px;height:16px;border-radius:50%;background:#fff;color:var(--ink);font:700 9px "Open Sans",sans-serif;display:flex;align-items:center;justify-content:center}
.burger{position:absolute;left:1100px;top:36px}

/* hero */
.hero{left:0;top:176px;width:1200px;height:185px;background:linear-gradient(90deg,#8a5a1c 0%,#c98d33 25%,#e2b25a 45%,#f2dcb0 65%,#f6e6c8 100%)}
.hero .copy{position:absolute;left:760px;top:10px;width:380px;text-align:center;color:#3b2a16}
.hero .big{font:300 62px/1 "Josefin Sans",sans-serif;letter-spacing:4px}
.hero .sub{font:300 34px/1.2 "Josefin Sans",sans-serif;letter-spacing:4px;margin-top:6px}
.hero .cta{position:absolute;left:782px;top:140px;width:310px;height:36px;background:#d99a2a;border:1px solid #f2cf86;color:#fff;font:400 19px "Josefin Sans",sans-serif;letter-spacing:2px;display:flex;align-items:center;justify-content:center}

/* product section */
.product-zone{left:0;top:361px;width:1200px;height:991px;background:var(--mist)}
.crumbs{position:absolute;left:81px;top:52px;font:11px "Open Sans",sans-serif;color:#444;display:flex;gap:8px}
.crumbs span.div{color:#aaa}
.gallery{position:absolute;left:69px;top:111px;width:517px;height:412px;background:radial-gradient(circle at 50% 48%,#f2edd6 0%,#d8cfa4 28%,#b7a56c 55%,#9e8a52 100%)}
.gallery .arrow{position:absolute;top:192px}
.thumb{position:absolute;top:531px;width:45px;height:60px}
.thumb.a{left:69px;background:linear-gradient(#c9c9c9,#a9a9a9)}
.thumb.b{left:120px;background:linear-gradient(#d7b56a,#8d6a2c)}
.info{position:absolute;left:657px;top:111px;width:440px}
.info h1{font:700 19px/1.2 "Montserrat",sans-serif;text-transform:uppercase}
.info .was{margin-top:14px;font:13px "Open Sans",sans-serif;color:var(--muted)}
.info .was s{color:#888}
.info .now{margin-top:8px;font:14px "Open Sans",sans-serif;color:#555}
.info .warn{margin-top:6px;font:11.5px "Open Sans",sans-serif;color:var(--alert)}
.info .label{margin-top:16px;font:700 13px "Open Sans",sans-serif}
.sizes{margin-top:8px;display:flex;gap:4px}
.sizes span{width:28px;height:22px;border-radius:11px;background:var(--pill);color:#fff;font:700 10px "Open Sans",sans-serif;display:flex;align-items:center;justify-content:center}
.qty{margin-top:8px;width:66px;height:36px;background:#fff;border:1px solid var(--line);position:relative;font:12px "Open Sans",sans-serif;padding:10px 0 0 16px}
.qty i{position:absolute;right:8px;font-style:normal;font-size:7px;color:#777}
.actions{margin-top:18px;display:flex;gap:6px}
.actions span{height:28px;padding:0 10px;border:1px solid #c9a24a;background:#fff;font:11px "Open Sans",sans-serif;display:flex;align-items:center}
.tabs{position:absolute;left:69px;top:658px;width:1061px;height:58px;border-bottom:1px solid var(--line);display:flex}
.tabs div{font:15px "Open Sans",sans-serif;color:#444;display:flex;align-items:center;justify-content:center}
.tabs .on{width:199px;background:var(--gold);color:#fff}
.tabs .t2{width:164px}
.tabs .t3{width:166px}
.desc{position:absolute;left:92px;top:743px;font:13.5px/26px "Open Sans",sans-serif;color:#444;list-style:none}

/* featured */
.featured{left:47px;top:1386px;width:1096px;height:329px;background:#fff;box-shadow:0 2px 6px rgba(0,0,0,.12)}
.featured .head{position:absolute;left:0;top:0;width:220px;height:53px;background:var(--nav);color:#fff;font:700 14px "Montserrat",sans-serif;display:flex;align-items:center;padding-left:22px}
.featured .rule{position:absolute;left:0;top:53px;width:1096px;height:1px;background:var(--line)}
.featured .nav-arrows{position:absolute;right:14px;top:16px;display:flex;gap:20px}
.items{position:absolute;left:32px;top:84px;display:flex;gap:28px;list-style:none}
.items li{width:150px;text-align:center}
.items .pic{width:150px;height:150px;border-radius:50%;border:5px solid #e4e4e4}
.items .coin-a{background:radial-gradient(circle,#e9e9e9,#9c9c9c)}
.items .coin-b{background:radial-gradient(circle,#f1f1f1,#a8a8a8)}
.items .ring{background:linear-gradient(#c8c3bd,#8f8a84)}
.items .set{background:linear-gradient(#2458a8,#0d2a5e)}
.items .watch{background:linear-gradient(#6a5e55,#2d2a28)}
.items .nm{margin-top:10px;font:600 11px/1.5 "Open Sans",sans-serif;min-height:34px}
.items .pr{margin-top:6px;font:600 11px "Open Sans",sans-serif}

/* recently viewed */
.recent-label{left:55px;top:1784px;width:231px;height:45px;background:var(--gold);border:3px solid #fbe0a0;color:#fff;font:700 16px "Cinzel",serif;letter-spacing:2px;display:flex;align-items:center;justify-content:center}
.card{top:1843px;width:345px;height:368px;background:#fff;box-shadow:0 1px 6px rgba(0,0,0,.12)}
.card .pic{position:absolute;top:2px;height:200px}
.card .date{position:absolute;left:16px;top:155px;width:44px;height:44px;background:var(--gold);color:#fff;text-align:center;font:700 10px/1.2 "Open Sans",sans-serif;padding-top:8px}
.card h3{position:absolute;left:16px;top:223px;width:310px;font:700 12px/1.5 "Open Sans",sans-serif;text-transform:uppercase}
.card p{position:absolute;left:16px;top:266px;width:310px;font:12px/1.6 "Open Sans",sans-serif;color:#666}
.card .more{position:absolute;left:16px;top:319px;width:102px;height:28px;border:1px solid #bbb;font:700 10.5px "Open Sans",sans-serif;display:flex;align-items:center;justify-content:center}

/* promises */
.promise{top:2258px;width:336px;height:180px;background:#fff;box-shadow:0 1px 6px rgba(0,0,0,.1);text-align:center;padding:44px 22px 0}
.promise h4{font:400 20px "Open Sans",sans-serif;color:#333}
.promise p{margin-top:12px;font:11.5px/1.6 "Open Sans",sans-serif;color:#555}

/* footer */
.signup{left:0;top:2503px;width:1200px;height:98px;background:var(--footer)}
.cards{position:absolute;left:55px;top:37px;display:flex;gap:4px}
.cards span{width:38px;height:24px;border-radius:3px;background:#fff}
.signup .title{position:absolute;left:449px;top:39px;font:600 15px "Open Sans",sans-serif;color:var(--gold);letter-spacing:.5px}
.signup .field{position:absolute;left:645px;top:32px;width:372px;height:34px;background:#fff;font:11px "Open Sans",sans-serif;color:#777;padding:11px 10px}
.signup .go{position:absolute;left:1021px;top:32px;width:122px;height:34px;background:var(--gold);color:#fff;font:700 11.5px "Open Sans",sans-serif;display:flex;align-items:center;justify-content:center;gap:5px}
.footer{left:0;top:2601px;width:1200px;height:294px;background:var(--footer-deep);border-top:1px solid #3a3f47}
.contact{position:absolute;left:55px;top:44px;width:345px;list-style:none}
.contact li{height:45px;border-bottom:1px solid #3e434b;display:flex;align-items:center;gap:14px;font:12.5px "Open Sans",sans-serif;color:var(--footer-text)}
.social{position:absolute;left:55px;top:238px;display:flex;gap:8px}
.social span{width:28px;height:28px;border-radius:50%;background:var(--gold)}
.col{position:absolute;top:38px}
.col h5{font:600 14px "Open Sans",sans-serif;color:var(--gold);letter-spacing:.5px}
.col ul{list-style:none;margin-top:14px}
.col li{font:11.5px/30px "Open Sans",sans-serif;color:var(--footer-text)}
.col li::before{content:"•";color:#777;margin-right:10px}
.copyright{left:0;top:2895px;width:1200px;height:46px;background:#1b1e23;color:#777;font:11px "Open Sans",sans-serif;display:flex;align-items:center;justify-content:center}
</style>
</head>
<body>

<header>
  <div class="abs ticker">
    <div class="rates">
      <span>GOLD $1,333.20</span><span class="up">▲$9.00</span><span class="sep"></span>
      <span>SILVER $16.64</span><span class="up">▲$0.12</span><span class="sep"></span>
      <span>PLATINUM $960.8</span>
    </div>
    <div class="phone">
      <svg width="13" height="13" viewBox="0 0 24 24"><path fill="#fff" d="M6.6 10.8a15 15 0 0 0 6.6 6.6l2.2-2.2c.3-.3.7-.4 1-.2 1.1.4 2.3.6 3.6.6.6 0 1 .4 1 1V20c0 .6-.4 1-1 1A17 17 0 0 1 3 4c0-.6.4-1 1-1h3.5c.6 0 1 .4 1 1 0 1.3.2 2.5.6 3.6.1.3 0 .7-.2 1z"/></svg>
      <span>205-410-2276, 205-418-3390</span>
    </div>
  </div>

  <div class="abs promo">
    <div class="note">NO MORE IN STATE SALES TAX ON GOLD/SILVER COINS &amp; BULLION! STARTING JUNE 1ST!</div>
    <div class="search">
      <input value="Search" aria-label="Search">
      <button aria-label="Search"><svg width="14" height="14" viewBox="0 0 24 24"><circle cx="10" cy="10" r="6.5" fill="none" stroke="#fff" stroke-width="2.6"/><path d="M15 15l6 6" stroke="#fff" stroke-width="2.6"/></svg></button>
    </div>
    <div class="login">LOGIN</div>
  </div>

  <nav class="abs mainnav">
    <div class="brand"><span class="mark"></span><span class="name">DOS</span></div>
    <ul class="menu">
      <li class="on">HOME</li><li>ABOUT</li><li>PRECIOUS METALS</li><li>FINE JEWELERY</li><li>FINE WATCHES</li><li>STERLING SILVER</li><li>BUY &amp; SELL</li><li>FAQ</li><li>CONTACT</li>
    </ul>
    <div class="cart">
      <svg width="26" height="24" viewBox="0 0 26 24"><path d="M1 2h4l3 13h13l3-9H7" fill="none" stroke="#fff" stroke-width="2.4"/><circle cx="10" cy="20" r="2" fill="#fff"/><circle cx="19" cy="20" r="2" fill="#fff"/></svg>
      <span class="count">2</span>
    </div>
    <svg class="burger" width="22" height="18" viewBox="0 0 22 18"><rect width="22" height="3" fill="#fff"/><rect y="7.5" width="22" height="3" fill="#fff"/><rect y="15" width="22" height="3" fill="#fff"/></svg>
  </nav>

  <section class="abs hero" role="img" aria-label="Close-up photograph of ornate gold earrings">
    <div class="copy">
      <div class="big">BEAUTIFUL</div>
      <div class="sub">FOREVER</div>
    </div>
    <div class="cta">BROWSE GOLD EARRINGS</div>
  </section>
</header>

<main>
  <section class="abs product-zone">
    <div class="crumbs"><span>Home</span><span class="div">/</span><span>Fine Jewelry</span><span class="div">/</span><span>Rings</span><span class="div">/</span><span>22k Indian Gold Ring</span></div>

    <div class="gallery" role="img" aria-label="Photograph of a brilliant round cut diamond">
      <svg class="arrow" style="left:24px" width="14" height="26" viewBox="0 0 14 26"><path d="M12 2L2 13l10 11" fill="none" stroke="#fff" stroke-width="2"/></svg>
      <svg class="arrow" style="right:24px" width="14" height="26" viewBox="0 0 14 26"><path d="M2 2l10 11L2 24" fill="none" stroke="#fff" stroke-width="2"/></svg>
    </div>
    <div class="thumb a" role="img" aria-label="Diamond thumbnail"></div>
    <div class="thumb b" role="img" aria-label="Gold ring thumbnail"></div>

    <div class="info">
      <h1>1.83ct K-Color I1 Brilliant Round GQL Cert.</h1>
      <div class="was"><s>$ 7,495.00</s> (50% off)</div>
      <div class="now">$ 6,495.00</div>
      <div class="warn">Warning: Last items in stock!</div>
      <div class="label">Select Size:</div>
      <div class="sizes"><span>4</span><span>5</span><span>6</span><span>7</span></div>
      <div class="label">Quantity</div>
      <div class="qty">1<i style="top:6px">▲</i><i style="bottom:6px">▼</i></div>
      <div class="actions"><span>ADD TO CART</span><span>BUY NOW</span></div>
    </div>

    <div class="tabs"><div class="on">Description</div><div class="t2">Details</div><div class="t3">Review</div></div>
    <ul class="desc">
      <li>Certified by GQL</li><li>Carat Weight- 1.83</li><li>Shape- Brilliant Round</li><li>Color- K</li><li>Clarity- I1</li><li>Cut- Very Good</li>
    </ul>
  </section>

  <section class="abs featured">
    <div class="head">FEATURED PRODUCTS</div>
    <div class="rule"></div>
    <div class="nav-arrows">
      <svg width="8" height="13" viewBox="0 0 8 13"><path d="M7 1L2 6.5 7 12" fill="none" stroke="#bbb" stroke-width="1.5"/></svg>
      <svg width="8" height="13" viewBox="0 0 8 13"><path d="M1 1l5 5.5L1 12" fill="none" stroke="#bbb" stroke-width="1.5"/></svg>
    </div>
    <ul class="items">
      <li><div class="pic coin-a" role="img" aria-label="Silver bullion coin"></div><div class="nm">C-WEED A.K.A. SEAWEED<br>(AAA)</div><div class="pr">$7 - $8 / GRAM</div></li>
      <li><div class="pic coin-b" role="img" aria-label="Silver eagle coin"></div><div class="nm">AK-47 (AAA)</div><div class="pr">$7 - $8 / GRAM</div></li>
      <li><div class="pic ring" role="img" aria-label="Diamond ring on a stand"></div><div class="nm">AK-47 (AAA)</div><div class="pr">$7 - $8 / GRAM</div></li>
      <li><div class="pic ring" role="img" aria-label="Diamond ring on a stand"></div><div class="nm">C-WEED A.K.A. SEAWEED<br>(AAA)</div><div class="pr">$7 - $8 / GRAM</div></li>
      <li><div class="pic set" role="img" aria-label="Sterling silver flatware set in a blue case"></div><div class="nm">C-WEED A.K.A. SEAWEED<br>(AAA)</div><div class="pr">$7 - $8 / GRAM</div></li>
      <li><div class="pic watch" role="img" aria-label="Luxury wristwatch"></div><div class="nm">AK-47 (AAA)</div><div class="pr">$7 - $8 / GRAM</div></li>
    </ul>
  </section>

  <div class="abs recent-label">RECENTLY VIEWED</div>

  <article class="abs card" style="left:55px">
    <div class="pic" role="img" aria-label="Princess cut diamond ring on a display" style="left:37px;width:271px;background:linear-gradient(#2a2a2a,#0d0d0d)"></div>
    <div class="date">14<br>APRIL</div>
    <h3>Lorem ipsum dolor sit amet, consectetur adipiscing</h3>
    <p>Pellentesque habitant morbi tristique senectus et netus et malesuada ...</p>
    <div class="more">READ MORE</div>
  </article>
  <article class="abs card" style="left:427px">
    <div class="pic" role="img" aria-label="Commemorative silver round" style="left:2px;width:341px;background:radial-gradient(circle at 50% 52%,#d6d6d6 0%,#8f8f8f 38%,#fff 40%,#fff 100%)"></div>
    <div class="date">14<br>APRIL</div>
    <h3>Lorem ipsum dolor sit amet, consectetur adipiscing</h3>
    <p>Pellentesque habitant morbi tristique senectus et netus et malesuada ...</p>
    <div class="more">READ MORE</div>
  </article>
  <article class="abs card" style="left:800px">
    <div class="pic" role="img" aria-label="Row of men's and women's wristwatches" style="left:2px;width:341px;background:linear-gradient(90deg,#fff 0%,#6d6560 12%,#4a4b52 35%,#2f4b7a 55%,#c9a48a 75%,#eee 90%,#fff 100%)"></div>
    <div class="date">14<br>APRIL</div>
    <h3>Lorem ipsum dolor sit amet, consectetur adipiscing</h3>
    <p>Pellentesque habitant morbi tristique senectus et netus et malesuada ...</p>
    <div class="more">READ MORE</div>
  </article>

  <div class="abs promise" style="left:78px"><h4>100% PRIVACY</h4><p>Offshore servers purged daily in privacy oriented jurisdictions assure you category best privacy</p></div>
  <div class="abs promise" style="left:441px"><h4>LARGEST VARIETY</h4><p>Carrying the largest variety in Vancouver, rest assured you will find a strain that will be just the right one to help you get through your time of need.</p></div>
  <div class="abs promise" style="left:804px"><h4>HIGHEST QUALITY</h4><p>All of our growers follow the strictest guidelines. No pesticides, long curing times and all strains are tested in house</p></div>
</main>

<footer>
  <div class="abs signup">
    <div class="cards"><span></span><span></span><span></span><span></span></div>
    <div class="title">SIGN UP FOR EMAILS</div>
    <div class="field">Enter your email address</div>
    <div class="go"><svg width="11" height="9" viewBox="0 0 11 9"><rect width="11" height="9" fill="#fff"/><path d="M0 0l5.5 5L11 0" fill="none" stroke="#f6be2c"/></svg>SUBSCRIBE</div>
  </div>

  <div class="abs footer">
    <ul class="contact">
      <li><svg width="11" height="14" viewBox="0 0 12 16"><path d="M6 0a6 6 0 0 0-6 6c0 4.5 6 10 6 10s6-5.5 6-10a6 6 0 0 0-6-6zm0 8.5A2.5 2.5 0 1 1 6 3.5a2.5 2.5 0 0 1 0 5z" fill="#c8cbd0"/></svg>4418 Larkspur Rd Irondale, AL 35210</li>
      <li><svg width="13" height="13" viewBox="0 0 14 14"><circle cx="7" cy="7" r="6" fill="none" stroke="#c8cbd0" stroke-width="1.5"/><path d="M7 3.5V7l2.5 1.5" fill="none" stroke="#c8cbd0" stroke-width="1.5"/></svg>Open M-F 9-5, Sat 10-2</li>
      <li><svg width="13" height="13" viewBox="0 0 24 24"><path fill="#c8cbd0" d="M6.6 10.8a15 15 0 0 0 6.6 6.6l2.2-2.2c.3-.3.7-.4 1-.2 1.1.4 2.3.6 3.6.6.6 0 1 .4 1 1V20c0 .6-.4 1-1 1A17 17 0 0 1 3 4c0-.6.4-1 1-1h3.5c.6 0 1 .4 1 1 0 1.3.2 2.5.6 3.6.1.3 0 .7-.2 1z"/></svg>205-410-2276 , 205-418-3390</li>
      <li><svg width="13" height="10" viewBox="0 0 13 10"><rect width="13" height="10" fill="#c8cbd0"/><path d="M0 0l6.5 5L13 0" fill="none" stroke="#20242a"/></svg>abc@example.com</li>
    </ul>
    <div class="social"><span></span><span></span></div>

    <div class="col" style="left:449px"><h5>QUICK LINKS</h5><ul><li>Blog</li><li>FAQs</li><li>Payment</li><li>Shipment</li><li>Where is my order?</li><li>Return policy</li></ul></div>
    <div class="col" style="left:686px"><h5>STYLE ADVISOR</h5><ul><li>Your Account</li><li>Information</li><li>Addresses</li><li>Discount</li><li>Orders History</li><li>Additional Information</li></ul></div>
    <div class="col" style="left:923px"><h5>INFORMATION</h5><ul><li>Site Map</li><li>Search Terms</li><li>Advanced Search</li><li>About Us</li><li>Contact Us</li><li>Suppliers</li></ul></div>
  </div>

  <div class="abs copyright">© 2017 Dixie Ore Smeltery. All Rights Reserved.</div>
</footer>

</body>
</html>
```